Typing Service Business Card Design

Need a new business card design for new logo update. The Keyline Crew is an outsourced typing service. We type audio / voice files into word documents. We are a professional service that is recognised in the industry over the past 15 years and have a strong connection to our brand. The final design should be professional, simple, yet effective.

Business

Contact Information for Business Card

Rosalind Varga
Director

rosalind@kbq.com.au
www.thekeylinecrewbase.com.au

```html
<!DOCTYPE html>
<html lang="en">
<head>
<meta charset="utf-8">
<title>The Keyline Crew — Business Card</title>
<link href="https://fonts.googleapis.com/css2?family=Arimo:wght@400;700&family=Jost:wght@400;500;600&display=swap" rel="stylesheet">
<style>
  :root {
    --pink: #e2259a;
    --ink: #141414;
    --paper: #ffffff;
    --backdrop: #e9e9eb;
    --muted: #2b2b2b;
  }
  * { box-sizing: border-box; margin: 0; padding: 0; }
  html, body {
    width: 1200px; height: 900px; overflow: hidden;
    background: var(--backdrop);
  }
  .canvas { position: relative; width: 1200px; height: 900px; }

  .card {
    position: absolute; left: 250px; width: 700px; height: 400px;
    overflow: hidden; border-radius: 3px;
    box-shadow: 0 6px 18px rgba(0,0,0,0.18);
  }
  .card--back { top: 30px; background: var(--ink); }
  .card--front { top: 470px; background: var(--paper); }

  .card__stripe {
    position: absolute; left: 0; right: 0; bottom: 10px; height: 8px;
    background: var(--pink);
  }

  .brand { position: absolute; font-family: "Arimo", Arial, sans-serif; }
  .brand__name {
    display: flex; align-items: center; gap: 12px;
    font-weight: 700; color: var(--pink); white-space: nowrap;
  }
  .brand__dot {
    display: inline-block; border-radius: 50%; background: var(--pink);
  }

  .card--back .brand { left: 0; right: 0; top: 150px; }
  .card--back .brand__name { justify-content: center; font-size: 40px; }
  .card--back .brand__dot { width: 18px; height: 18px; }

  .card--front .brand { left: 48px; top: 124px; }
  .card--front .brand__name { font-size: 27px; gap: 9px; }
  .card--front .brand__dot { width: 12px; height: 12px; }

  .service-line {
    position: absolute; font-family: "Arimo", Arial, sans-serif;
    font-weight: 400; white-space: nowrap;
  }
  .card--back .service-line {
    left: 0; right: 0; top: 212px; text-align: center;
    color: var(--paper); font-size: 24px;
  }
  .card--front .service-line {
    left: 48px; top: 166px; color: var(--ink); font-size: 17px;
  }

  .contact {
    position: absolute; left: 385px; top: 222px;
    font-family: "Jost", "Futura", sans-serif; color: var(--muted);
  }
  .contact__name { font-size: 29px; font-weight: 600; color: var(--pink); line-height: 1.1; }
  .contact__role { font-size: 17px; margin: 4px 0 12px; }
  .contact__list {
    list-style: none; border-left: 2px solid var(--pink); padding-left: 8px;
  }
  .contact__item {
    display: flex; align-items: center; gap: 9px;
    font-size: 17px; line-height: 1.45;
  }
  .contact__icon { width: 15px; height: 15px; flex: none; }
</style>
</head>
<body>
<main class="canvas">

  <section class="card card--back" aria-label="Card back">
    <div class="brand">
      <div class="brand__name"><span class="brand__dot"></span>The Keyline Crew</div>
    </div>
    <p class="service-line">Audio in. Pages out.</p>
    <div class="card__stripe"></div>
  </section>

  <section class="card card--front" aria-label="Card front">
    <div class="brand">
      <div class="brand__name"><span class="brand__dot"></span>The Keyline Crew</div>
    </div>
    <p class="service-line">Audio in. Pages out.</p>

    <div class="contact">
      <p class="contact__name">Rosalind Varga</p>
      <p class="contact__role">Director</p>
      <ul class="contact__list">
        <li class="contact__item">
          <svg class="contact__icon" viewBox="0 0 16 16" aria-hidden="true">
            <rect x="0" y="0" width="16" height="16" rx="3" fill="var(--pink)"/>
            <rect x="3" y="4.5" width="10" height="7" fill="none" stroke="#fff" stroke-width="1.3"/>
            <path d="M3 4.5 L8 8.6 L13 4.5" fill="none" stroke="#fff" stroke-width="1.3"/>
          </svg>
          rosalind@kbq.com.au
        </li>
        <li class="contact__item">
          <svg class="contact__icon" viewBox="0 0 16 16" aria-hidden="true">
            <rect x="0" y="0" width="16" height="16" rx="3" fill="var(--pink)"/>
            <circle cx="8" cy="8" r="5" fill="none" stroke="#fff" stroke-width="1.2"/>
            <ellipse cx="8" cy="8" rx="2.2" ry="5" fill="none" stroke="#fff" stroke-width="1"/>
            <line x1="3" y1="8" x2="13" y2="8" stroke="#fff" stroke-width="1"/>
          </svg>
          www.thekeylinecrewbase.com.au
        </li>
      </ul>
    </div>
    <div class="card__stripe"></div>
  </section>

</main>
</body>
</html>
```